Hello my name is Colin, I am Starting a business called Harbor Health and fitness and am in need of a memorable business card.
It is a personal training studio. I have added the logo that i would like to be on the left center om my business card. i would like room left up the top for a heading sentence such as. "Is your body shocking for all the wrong reasons". there must be room left on the right of the logo below the main heading for 3 sub headings.
then under those 3 headings and logo room for another larger heading eg. "give me a call and learn how to eat chocolate, drink bear and have great sex". in what room is left i would like to be used for my contact details, use I'm Colin Fairweather your fitness expert on the left then on the right Phone, Email and website space in at least 12 Point. Very specific i know :) now onto the back, for the back i would like an eye catching graphic and room for one main headline and 3 bullet points centered just write anything i will choose what to put in them when i pick a winner. Thank you very much for sticking through all of that :) i appreciate you taking the time to read it and hopefully undergo designing me a business card.
I can't wait to see the designs!

Target Market(s)

slightly more towards females although it would probably be best if it was targeted towards both sexes

Industry/Entity Type

Training

Requirements
Nice to have
• I would love to see if anyone could come up with a design that would really make my card stand out and be memorable.
Should not have
• tacky fitness photos of abs and muscles etc.

```html
<!DOCTYPE html>
<html lang="en">
<head>
<meta charset="utf-8">
<title>Harbor Health and Fitness – Business Card</title>
<link rel="stylesheet" href="https://fonts.googleapis.com/css2?family=Questrial&family=Open+Sans:ital,wght@0,700;1,600&display=swap">
<style>
  :root {
    --page-bg: #e9e7e3;
    --card-white: #ffffff;
    --navy: #1b2f6e;
    --ink: #1d1d24;
    --divider-fade: #ffffff;
    --divider-mid: #2a5bc0;
    --back-deep: #1c3268;
    --back-mid: #27459a;
    --back-light: #3658b4;
    --back-text: #f2f5fc;
  }
  * { margin: 0; padding: 0; box-sizing: border-box; }
  html, body { width: 1102px; height: 1200px; overflow: hidden; }
  body { background: var(--page-bg); position: relative; }

  .card {
    position: absolute;
    left: 101px;
    width: 900px;
    height: 514px;
    border-radius: 4px;
    box-shadow: 0 6px 22px rgba(0,0,0,0.18);
    overflow: hidden;
  }

  /* Front */
  .card-front { top: 60px; background: var(--card-white); }
  .front-quote {
    position: absolute;
    top: 74px; left: 0; right: 0;
    text-align: center;
    font-family: "Open Sans", sans-serif;
    font-style: italic;
    font-weight: 600;
    font-size: 17px;
    color: var(--navy);
  }
  .brand {
    position: absolute;
    left: 110px; top: 200px;
    color: var(--navy);
    font-family: "Questrial", sans-serif;
    display: flex;
    flex-direction: column;
    align-items: flex-end;
  }
  .brand-name { font-size: 88px; line-height: 0.95; letter-spacing: -1px; }
  .brand-tagline { font-size: 24px; margin-top: 4px; }
  .divider {
    position: absolute;
    left: 455px; top: 160px;
    width: 3px; height: 190px;
    background: linear-gradient(to bottom, var(--divider-fade), var(--divider-mid) 55%, var(--divider-fade));
  }
  .contact {
    position: absolute;
    left: 520px; top: 172px;
    list-style: none;
    font-family: "Questrial", sans-serif;
    font-size: 25px;
    color: var(--ink);
  }
  .contact li { display: flex; align-items: center; gap: 14px; height: 40px; white-space: nowrap; }
  .contact svg { width: 20px; height: 20px; flex: none; fill: var(--navy); }
  .trainer-intro {
    position: absolute;
    left: 110px; bottom: 70px;
    font-family: "Open Sans", sans-serif;
    font-weight: 700;
    font-size: 17px;
    color: var(--ink);
  }

  /* Back */
  .card-back {
    top: 626px;
    background: radial-gradient(ellipse at 45% 40%, var(--back-light) 0%, var(--back-mid) 45%, var(--back-deep) 100%);
  }
  .back-texture {
    position: absolute; inset: 0;
    background: linear-gradient(120deg, rgba(255,255,255,0.06), rgba(255,255,255,0) 40%, rgba(255,255,255,0.05) 75%, rgba(0,0,0,0.08));
  }
  .back-copy {
    position: absolute;
    left: 0; right: 0; top: 150px;
    text-align: center;
    font-family: "Questrial", sans-serif;
    color: var(--back-text);
  }
  .back-heading { font-size: 30px; font-weight: 400; margin-bottom: 20px; }
  .back-points { list-style: none; font-size: 26px; line-height: 1.3; }
</style>
</head>
<body>
  <section class="card card-front">
    <p class="front-quote">"Give me a call and learn how to eat chocolate, drink bear and have great sex"</p>
    <div class="brand">
      <span class="brand-name">Harbor</span>
      <span class="brand-tagline">Health and Fitness</span>
    </div>
    <div class="divider"></div>
    <ul class="contact">
      <li>
        <svg viewBox="0 0 24 24" aria-hidden="true"><path d="M6.6 10.8a15.1 15.1 0 0 0 6.6 6.6l2.2-2.2a1 1 0 0 1 1-.25 11.4 11.4 0 0 0 3.6.57 1 1 0 0 1 1 1V20a1 1 0 0 1-1 1A17 17 0 0 1 3 4a1 1 0 0 1 1-1h3.5a1 1 0 0 1 1 1c0 1.25.2 2.45.57 3.6a1 1 0 0 1-.25 1z"/></svg>
        <span>555-218-4071</span>
      </li>
      <li>
        <svg viewBox="0 0 24 24" aria-hidden="true"><path d="M2 5h20v14H2zm2 2v.4l8 5.6 8-5.6V7zm0 2.8V17h16V9.8l-8 5.6z"/></svg>
        <span>info@harborfitstudio.com</span>
      </li>
      <li>
        <svg viewBox="0 0 24 24" aria-hidden="true"><path d="M12 2a10 10 0 1 0 0 20 10 10 0 0 0 0-20zm6.9 6h-3a15.6 15.6 0 0 0-1.4-3.6A8 8 0 0 1 18.9 8zM12 4a14 14 0 0 1 1.9 4h-3.8A14 14 0 0 1 12 4zM4.3 14a8.2 8.2 0 0 1 0-4h3.4a16.5 16.5 0 0 0 0 4zm.8 2h3a15.6 15.6 0 0 0 1.4 3.6A8 8 0 0 1 5.1 16zm3-8h-3a8 8 0 0 1 4.4-3.6A15.6 15.6 0 0 0 8.1 8zM12 20a14 14 0 0 1-1.9-4h3.8A14 14 0 0 1 12 20zm2.3-6H9.7a14.7 14.7 0 0 1 0-4h4.6a14.7 14.7 0 0 1 0 4zm.2 5.6a15.6 15.6 0 0 0 1.4-3.6h3a8 8 0 0 1-4.4 3.6zm1.8-5.6a16.5 16.5 0 0 0 0-4h3.4a8.2 8.2 0 0 1 0 4z"/></svg>
        <span>www.harborfitstudio.com</span>
      </li>
    </ul>
    <p class="trainer-intro">I'm Colin Fairweather your fitness expert !</p>
  </section>

  <section class="card card-back">
    <div class="back-texture" role="img" aria-label="Soft blue backdrop with scattered translucent squares and faint fitness figures"></div>
    <div class="back-copy">
      <h2 class="back-heading">Heading</h2>
      <ul class="back-points">
        <li>- First Line sample here</li>
        <li>- Second Line sample here</li>
        <li>- Third line sample here</li>
      </ul>
    </div>
  </section>
</body>
</html>
```